Cedarbrook Lane Allies Stationery

Use attached logo for stationery
Stationery, Letterhead and Envelope + Business cards

Tag line: Walking alongside those doing the work of the Gospel

```html
<!DOCTYPE html>
<html lang="en">
<head>
<meta charset="utf-8">
<title>Cedarbrook Lane Allies – Business Card</title>
<link rel="stylesheet" href="https://fonts.googleapis.com/css2?family=Roboto:ital,wght@0,400;0,700;1,400;1,700&display=swap">
<style>
  :root {
    --backdrop: #151516;
    --card: #2e2f31;
    --card-light: #3a3b3e;
    --sky: #6fb3d6;
    --navy: #1f5f9a;
    --gold: #e5b51d;
    --paper-text: #d9d9d9;
  }
  html, body {
    margin: 0;
    width: 1200px;
    height: 1200px;
    overflow: hidden;
    background: var(--backdrop);
    font-family: "Roboto", sans-serif;
  }
  .business-card {
    position: absolute;
    left: 100px;
    top: 315px;
    width: 1000px;
    height: 570px;
    background: radial-gradient(ellipse at 55% 55%, var(--card-light), var(--card) 70%);
    box-shadow: 0 20px 50px rgba(0,0,0,.6);
  }
  .brand {
    position: absolute;
    left: 70px;
    top: 80px;
    display: flex;
    align-items: center;
    gap: 16px;
  }
  .brand-dot {
    width: 26px;
    height: 26px;
    border-radius: 50%;
    background: var(--navy);
  }
  .brand-name {
    font-size: 38px;
    font-weight: 700;
    color: var(--navy);
    letter-spacing: .5px;
  }
  .divider {
    position: absolute;
    left: 70px;
    top: 185px;
    width: 600px;
    height: 2px;
    background: var(--sky);
  }
  .person {
    position: absolute;
    right: 70px;
    top: 155px;
    text-align: right;
  }
  .person-name {
    font-size: 40px;
    font-weight: 700;
    font-style: italic;
    color: var(--sky);
    margin: 0;
  }
  .person-title {
    font-size: 22px;
    font-style: italic;
    color: var(--gold);
    margin: 4px 0 0;
  }
  .address {
    position: absolute;
    left: 70px;
    top: 330px;
    font-size: 21px;
    font-style: italic;
    line-height: 1.45;
    color: var(--paper-text);
  }
  .contacts {
    position: absolute;
    right: 70px;
    bottom: 70px;
    list-style: none;
    margin: 0;
    padding: 0;
    font-size: 22px;
    font-style: italic;
    color: var(--paper-text);
  }
  .contacts li {
    display: flex;
    justify-content: flex-end;
    align-items: center;
    gap: 14px;
    line-height: 1.6;
  }
  .contacts svg { width: 22px; height: 22px; fill: none; stroke: var(--gold); stroke-width: 2; }
  .contacts .solid { fill: var(--gold); stroke: none; }
</style>
</head>
<body>
  <section class="business-card">
    <div class="brand">
      <span class="brand-dot"></span>
      <span class="brand-name">Cedarbrook Lane Allies</span>
    </div>
    <div class="divider"></div>

    <div class="person">
      <p class="person-name">Daniel Hart</p>
      <p class="person-title">Managing Director</p>
    </div>

    <address class="address">
      48 B Orchard Mill Lane<br>
      Greenfield, SC 29110
    </address>

    <ul class="contacts">
      <li>(803) 555-0147
        <svg viewBox="0 0 24 24"><path class="solid" d="M6.6 10.8a15 15 0 006.6 6.6l2.2-2.2a1 1 0 011-.25 11.4 11.4 0 003.6.6 1 1 0 011 1V20a1 1 0 01-1 1A17 17 0 013 4a1 1 0 011-1h3.5a1 1 0 011 1 11.4 11.4 0 00.6 3.6 1 1 0 01-.25 1z"/></svg>
      </li>
      <li>info@cedarbrooklaneallies.org
        <svg viewBox="0 0 24 24"><rect x="2" y="5" width="20" height="14" rx="1"/><path d="M2 6l10 7 10-7"/></svg>
      </li>
      <li>www.cedarbrooklaneallies.org
        <svg viewBox="0 0 24 24"><circle cx="12" cy="12" r="9.5"/><ellipse cx="12" cy="12" rx="4" ry="9.5"/><path d="M2.5 12h19M4 7h16M4 17h16"/></svg>
      </li>
    </ul>
  </section>
</body>
</html>
```